RM Cargoline businesscard project

RM Cargoline Ltd is a freshly founded small (3 employees), young (average age is 30 years) company, living from the road transportation market without own tools.
We would like to have an impressive, new-line, cool busines card for a freshly founded forwarding company on an overcrowded market which raises attention and makes the potential partners eager to work with us.

Target Market(s)

The main profile of the company is logistic/forwarding on road.

Industry/Entity Type

Freight Forwarding

Contact Information for Business Card

Name: Berki Zsófia
Title: general manager
mobile nr: +36-70/482-5193
fax nr: +36-1/534-9061
e-mail: zsofia.berki@rmcargoline.example
info@rmcargoline.example
website address: http://www.rmcargoline.example
and if possible maybe some funny or helpful info on the back

Requirements
Must have
• contact details above
Nice to have
• some really nice and catching back-side (info, graphics, useful tool info... anything)
Should not have
• trucks, road, ship, airplane on it...

```html
<!DOCTYPE html>
<html lang="en">
<head>
<meta charset="utf-8">
<title>RM Cargoline – Business Card</title>
<link href="https://fonts.googleapis.com/css2?family=Lato:wght@400;700;900&display=swap" rel="stylesheet">
<style>
  :root {
    --backdrop: #2b2b2d;
    --blue-deep: #3674c2;
    --blue-light: #6ea2dc;
    --paper: #f4f3f2;
    --ink: #2a2a2c;
    --white: #ffffff;
    --divider: #9a9a9a;
  }
  * { box-sizing: border-box; margin: 0; padding: 0; }
  html, body {
    width: 1200px; height: 900px; overflow: hidden;
    background: var(--backdrop);
    font-family: "Lato", Arial, sans-serif;
  }
  .card {
    position: absolute; left: 250px; width: 700px; height: 390px;
    box-shadow: 0 6px 18px rgba(0,0,0,.45);
    overflow: hidden;
  }
  .card-back { top: 45px; }
  .card-back svg { display: block; }
  .card-front { top: 465px; display: flex; }
  .brand-panel {
    width: 300px; height: 100%;
    background: var(--paper);
    display: flex; align-items: center; justify-content: center; gap: 14px;
  }
  .brand-mark { width: 24px; height: 24px; background: var(--blue-deep); flex: none; }
  .brand-name { font-weight: 700; font-size: 36px; color: var(--ink); letter-spacing: -.5px; white-space: nowrap; }
  .panel-divider {
    width: 10px; height: 100%;
    background: repeating-linear-gradient(45deg, var(--divider) 0 2px, #c8c8c8 2px 4px);
  }
  .contact-panel {
    flex: 1; height: 100%;
    background: linear-gradient(135deg, var(--blue-deep), var(--blue-light));
    color: var(--white);
    padding: 62px 30px 0 96px;
  }
  .person-name { font-weight: 700; font-size: 19px; }
  .person-title { font-size: 14px; margin-left: 12px; margin-top: 1px; }
  .contact-list { list-style: none; margin-top: 48px; font-size: 15px; line-height: 21px; }
  .contact-list li { display: flex; align-items: center; }
  .contact-icon { width: 30px; flex: none; }
  .contact-icon svg { width: 15px; height: 13px; display: block; fill: var(--white); }
</style>
</head>
<body>

<section class="card card-back" aria-label="Card back">
  <svg width="700" height="390" viewBox="0 0 700 390">
    <defs>
      <linearGradient id="back-fill" x1="0" y1="1" x2="1" y2="0">
        <stop offset="0" stop-color="#3674c2"/>
        <stop offset="1" stop-color="#6ea2dc"/>
      </linearGradient>
      <radialGradient id="mode-fill" cx=".5" cy=".5" r=".5">
        <stop offset="0" stop-color="#3f7cc8"/>
        <stop offset="1" stop-color="#6a9dd8"/>
      </radialGradient>
    </defs>
    <rect width="700" height="390" fill="url(#back-fill)"/>
    <rect x="140" y="28" width="420" height="84" fill="none" stroke="#fff" stroke-width="1.5" stroke-dasharray="3 3" opacity=".85"/>
    <text x="350" y="76" text-anchor="middle" fill="#fff" font-family="Lato, sans-serif" font-weight="900" font-size="38">What is LOGISTICS?</text>
    <text x="350" y="98" text-anchor="middle" fill="#fff" font-family="Lato, sans-serif" font-size="11">Logistics is enabling things to be in the right destination at a given time.</text>
    <g stroke="#fff" stroke-width="1.4" stroke-dasharray="2 3" opacity=".9">
      <line x1="300" y1="112" x2="125" y2="258"/>
      <line x1="325" y1="112" x2="228" y2="262"/>
      <line x1="350" y1="112" x2="330" y2="256"/>
      <line x1="375" y1="112" x2="430" y2="240"/>
      <line x1="400" y1="112" x2="530" y2="204"/>
    </g>
    <g class="transport-modes">
      <g role="img" aria-label="Transport mode icon: truck">
        <circle cx="125" cy="296" r="38" fill="#fff"/>
        <ellipse cx="125" cy="296" rx="22" ry="13" fill="url(#mode-fill)"/>
      </g>
      <g role="img" aria-label="Transport mode icon: pickup truck">
        <circle cx="228" cy="300" r="38" fill="#fff"/>
        <ellipse cx="228" cy="300" rx="22" ry="12" fill="url(#mode-fill)"/>
      </g>
      <g role="img" aria-label="Transport mode icon: ship">
        <circle cx="330" cy="294" r="38" fill="#fff"/>
        <ellipse cx="330" cy="294" rx="24" ry="12" fill="url(#mode-fill)"/>
      </g>
      <g role="img" aria-label="Transport mode icon: airplane">
        <circle cx="432" cy="278" r="38" fill="#fff"/>
        <ellipse cx="432" cy="278" rx="23" ry="12" fill="url(#mode-fill)"/>
      </g>
      <g role="img" aria-label="Transport mode icon: train">
        <circle cx="534" cy="242" r="38" fill="#fff"/>
        <ellipse cx="534" cy="242" rx="16" ry="20" fill="url(#mode-fill)"/>
      </g>
    </g>
    <text x="330" y="368" text-anchor="middle" fill="#fff" font-family="Lato, sans-serif" font-weight="700" font-size="15">Logistics Different Modes of Transportation</text>
  </svg>
</section>

<section class="card card-front" aria-label="Card front">
  <div class="brand-panel">
    <span class="brand-mark"></span>
    <span class="brand-name">RM Cargoline</span>
  </div>
  <div class="panel-divider"></div>
  <div class="contact-panel">
    <p class="person-name">Berki Zsófia</p>
    <p class="person-title">General Manager</p>
    <ul class="contact-list">
      <li><span class="contact-icon"><svg viewBox="0 0 15 13"><path d="M1 4c0-2 3-3 6.5-3S14 2 14 4v1h-3V4H4v1H1z M3 6h9l2 6H1z"/></svg></span><span>+36-70/482-5193</span></li>
      <li><span class="contact-icon"><svg viewBox="0 0 15 13"><path d="M4 0h7v4H4z M1 5h13v6h-3v2H4v-2H1z"/></svg></span><span>+36-1/534-9061</span></li>
      <li><span class="contact-icon"><svg viewBox="0 0 15 13"><path d="M0 0h15v9H0z M1.5 1.5v6h12v-6z M5 10h5v1h2v2H3v-2h2z" fill-rule="evenodd"/></svg></span><span>www.rmcargoline.example</span></li>
      <li><span class="contact-icon"><svg viewBox="0 0 15 13"><path d="M0 2h15v10H0z M1 3l6.5 5L14 3z" fill-rule="evenodd"/></svg></span><span>zsofia.berki@rmcargoline.example</span></li>
      <li><span class="contact-icon"></span><span>info@rmcargoline.example</span></li>
    </ul>
  </div>
</section>

</body>
</html>
```